Book cover for a book about time management for women

We need a book cover for a book about time management for women written by a woman. Even though the book has a provocative title "Calendar rebellion" based on the seminars the author holds for women seeking the change in their life, it has nothing to do with the words themselves. The subtitle is "Steer each day by choice. An opening guide on hour mastery among ladies"

Preferred fonts (not necessarily):
Plus Jakarta Sans
Tiempos Headline

Preferred colours (not necessarily):
- orange
- pastel "highlighters"

We look for a simple/clean design that catches the attention of the women without too many graphic elements.

Target Market(s)

Women that want to change and organise their life

Industry/Entity Type

productivity, marketing, work-life balance

Font styles to use
Other font styles liked:
• Plus Jakarta Sans, Tiempos Headline

Colors
F0912C
F2A743
F7CA91
FBE8D2
FDF5EE
A7469A
B969AE
D3A5CF
EDDBEB
F8F0F9

Requirements
Must have
• Famine feeling as the target audience are women with drive to better life
Should not have
• No explicit images or sexually motivated themes

```html
<!DOCTYPE html>
<html lang="en">
<head>
<meta charset="utf-8">
<title>Calendar Rebellion – Book Cover</title>
<link rel="stylesheet" href="https://fonts.googleapis.com/css2?family=Playfair+Display:wght@600;700&family=Plus+Jakarta+Sans:wght@300;400;500&display=swap">
<style>
  :root {
    --stage: #000000;
    --orange: #F0912C;
    --orange-soft: #F2A743;
    --purple: #7A2D78;
    --purple-deep: #5E1F5C;
    --purple-accent: #A7469A;
    --cream: #FDF5EE;
    --ink: #1A1418;
  }
  * { margin: 0; padding: 0; box-sizing: border-box; }
  html, body {
    width: 1200px;
    height: 1200px;
    overflow: hidden;
    background: var(--stage);
  }
  .canvas {
    position: relative;
    width: 1200px;
    height: 1200px;
    background: var(--stage);
  }
  .cover {
    position: absolute;
    left: 360px;
    top: 240px;
    width: 480px;
    height: 720px;
    display: flex;
    flex-direction: column;
    overflow: hidden;
  }
  .cover-hero {
    position: relative;
    height: 329px;
    background:
      radial-gradient(ellipse 40% 22% at 45% 50%, #FFE9B8 0%, rgba(255,205,130,0.85) 35%, rgba(230,160,90,0) 100%),
      radial-gradient(ellipse 75% 45% at 50% 90%, #8A6A40 0%, #6B5237 45%, rgba(80,60,50,0) 100%),
      linear-gradient(180deg, #5C4A5A 0%, #9A8690 22%, #C9B7A8 42%, #E3B67E 55%, #A8834F 72%, #5A4532 100%);
  }
  .hero-tagline {
    position: absolute;
    top: 30px;
    left: 0;
    right: 0;
    text-align: center;
    font-family: 'Plus Jakarta Sans', sans-serif;
    font-weight: 400;
    font-size: 18.5px;
    line-height: 1.3;
    letter-spacing: 0.14em;
    color: var(--cream);
    text-transform: uppercase;
  }
  .cover-divider {
    height: 9px;
    background: var(--purple-accent);
  }
  .cover-title-panel {
    flex: 1;
    background: var(--orange);
    display: flex;
    flex-direction: column;
    align-items: center;
    padding-top: 24px;
  }
  .title-lead {
    font-family: 'Playfair Display', serif;
    font-weight: 700;
    font-size: 50px;
    line-height: 1;
    letter-spacing: -0.01em;
    color: var(--purple-deep);
    text-transform: uppercase;
  }
  .title-main {
    font-family: 'Playfair Display', serif;
    font-weight: 600;
    font-size: 66px;
    line-height: 1.18;
    letter-spacing: -0.01em;
    color: var(--purple-deep);
    text-transform: uppercase;
    margin-top: 10px;
  }
  .subtitle {
    margin-top: 14px;
    text-align: center;
    font-family: 'Plus Jakarta Sans', sans-serif;
    font-weight: 300;
    font-size: 37px;
    line-height: 1.15;
    letter-spacing: 0.12em;
    color: var(--ink);
    text-transform: uppercase;
  }
  .cover-author-band {
    height: 69px;
    background: var(--purple);
    display: flex;
    align-items: center;
    justify-content: center;
  }
  .author-name {
    font-family: 'Plus Jakarta Sans', sans-serif;
    font-weight: 500;
    font-size: 20px;
    letter-spacing: 0.14em;
    color: var(--cream);
    text-transform: uppercase;
  }
</style>
</head>
<body>
  <main class="canvas">
    <article class="cover">
      <section class="cover-hero" role="img" aria-label="Photo of a woman in silhouette standing on the centre of a large clock face with gears, backlit by a golden sunrise">
        <p class="hero-tagline">An opening guide on<br>hour mastery among ladies</p>
      </section>
      <div class="cover-divider"></div>
      <section class="cover-title-panel">
        <h1>
          <span class="title-lead" style="display:block;text-align:center;">Calendar</span>
          <span class="title-main" style="display:block;text-align:center;">Rebellion</span>
        </h1>
        <p class="subtitle">Steer each day<br>by choice</p>
      </section>
      <footer class="cover-author-band">
        <p class="author-name">Author Names</p>
      </footer>
    </article>
  </main>
</body>
</html>
```